Post storm repair flyer

looking for an eye catching 6x9 postcard to send out to single family home owners advertising a "Post Storm Repair Special" explaining that after the recent hurricanes its very important to have your roof checked and any repairs fixed right away before they become a bigger more costly problem and that even though your home wasn't directly hit by the storm the high wind gust could've cause unseen damage.
offer $200 off any repair *some rules may apply
Lark Roofing
888.417.LARK
www.LarkRoofing.example

Roofing

```html
<!DOCTYPE html>
<html lang="en">
<head>
<meta charset="utf-8">
<title>Lark Roofing – Post Storm Repair Special Postcard</title>
<link href="https://fonts.googleapis.com/css2?family=Poppins:wght@400;500;600;700&display=swap" rel="stylesheet">
<style>
  :root {
    --stage: #d9d9db;
    --paper: #ffffff;
    --paper-shade: #f1f1f2;
    --gold: #e5aa22;
    --charcoal: #58585a;
    --ink: #2b2b2d;
    --steel-blue: #3f6685;
    --stamp: #b9b9bc;
    --photo-sky: #8fa7bf;
    --photo-roof: #6d6f75;
    --photo-earth: #8a6a52;
  }
  * { box-sizing: border-box; margin: 0; padding: 0; }
  html, body { width: 1143px; height: 1200px; overflow: hidden; }
  body {
    background: var(--stage);
    font-family: "Poppins", Arial, sans-serif;
    position: relative;
  }
  .postcard {
    position: absolute;
    left: 144px;
    width: 855px;
    height: 570px;
    background: var(--paper);
    overflow: hidden;
    box-shadow: 0 6px 18px rgba(0,0,0,0.22);
  }
  .postcard--front { top: 20px; }
  .postcard--back { top: 610px; }
  .postcard svg.artwork { position: absolute; inset: 0; }
  .text { position: absolute; }

  /* front */
  .brand-name {
    color: var(--ink);
    font-weight: 600;
    letter-spacing: 0.5px;
  }
  .front-brand { left: 30px; top: 100px; width: 300px; text-align: center; font-size: 25px; line-height: 1.2; }
  .headline {
    left: 0; top: 300px; width: 855px; text-align: center;
    color: var(--paper); font-weight: 700; font-size: 45px; line-height: 70px;
    letter-spacing: 0.3px;
  }
  .storm-message {
    left: 55px; top: 400px; width: 745px; text-align: center;
    color: var(--ink); font-size: 13.6px; line-height: 18px;
  }
  .contact-name { color: var(--paper); font-size: 20px; line-height: 1; font-weight: 400; }
  .contact-phone { color: var(--paper); font-size: 35px; font-weight: 700; line-height: 1.1; }
  .front-contact { left: 215px; top: 492px; }
  .front-web {
    left: 530px; top: 524px; color: var(--paper); font-weight: 600; font-size: 21px;
  }

  /* back */
  .offer { left: 60px; top: 340px; color: var(--paper); font-weight: 600; font-size: 19px; line-height: 1.1; }
  .offer strong { color: var(--gold); font-size: 29px; font-weight: 700; }
  .offer small { display: block; font-weight: 400; font-size: 14px; }
  .back-contact { left: 92px; top: 427px; color: var(--charcoal); }
  .back-contact .contact-name { color: var(--charcoal); font-size: 27px; }
  .back-contact .contact-phone { color: var(--charcoal); font-size: 42px; }
  .back-contact .contact-web { font-size: 19px; font-weight: 600; margin-left: 62px; color: var(--charcoal); }
  .back-brand { left: 445px; top: 130px; width: 200px; text-align: center; font-size: 15px; }
</style>
</head>
<body>

<section class="postcard postcard--front" aria-label="Postcard front">
  <svg class="artwork" width="855" height="570" viewBox="0 0 855 570">
    <defs>
      <linearGradient id="house-photo" x1="0" y1="0" x2="1" y2="1">
        <stop offset="0" stop-color="#c9d6e3"/>
        <stop offset="0.5" stop-color="var(--photo-sky)"/>
        <stop offset="1" stop-color="var(--photo-roof)"/>
      </linearGradient>
      <linearGradient id="worker-photo" x1="0" y1="0" x2="1" y2="1">
        <stop offset="0" stop-color="#7c8591"/>
        <stop offset="1" stop-color="#b8703f"/>
      </linearGradient>
    </defs>
    <polygon points="0,0 340,0 180,210 0,90" fill="var(--paper-shade)"/>
    <polygon points="285,0 345,0 545,218 745,282 855,200 855,300 0,300 0,290 470,290" fill="var(--gold)"/>
    <polygon points="345,0 855,0 855,188 745,268 545,205" fill="url(#house-photo)" role="img" aria-label="Photo of a two-storey house with a new shingle roof"/>
    <polyline points="330,0 540,230 745,292 855,212" fill="none" stroke="var(--ink)" stroke-width="4"/>
    <polygon points="560,55 656,110 656,220 560,275 464,220 464,110" fill="var(--paper)" stroke="var(--gold)" stroke-width="6"/>
    <polygon points="560,72 641,119 641,211 560,258 479,211 479,119" fill="url(#worker-photo)" role="img" aria-label="Photo of a roofer in safety gear repairing roof tiles"/>
    <rect x="0" y="290" width="855" height="86" fill="var(--gold)"/>
    <polygon points="0,440 0,570 195,570" fill="var(--steel-blue)"/>
    <polygon points="140,478 855,478 855,570 210,570" fill="var(--charcoal)"/>
    <line x1="502" y1="493" x2="502" y2="555" stroke="var(--gold)" stroke-width="2"/>
    <circle cx="666" cy="507" r="11" fill="var(--gold)"/>
    <g fill="none" stroke="var(--paper)" stroke-width="1.3">
      <circle cx="666" cy="507" r="6"/>
      <ellipse cx="666" cy="507" rx="2.6" ry="6"/>
      <line x1="660" y1="507" x2="672" y2="507"/>
    </g>
  </svg>
  <p class="text brand-name front-brand">LARKROOFING.EXAMPLE</p>
  <h1 class="text headline">POST STORM REPAIR SPECIAL</h1>
  <p class="text storm-message">After the recent hurricanes its very important to have your roof checked and any repairs fixed right away before they become a bigger more costly problem and that even though your home wasn't directly hit by the storm the high wind gust could've cause unseen damage.</p>
  <div class="text front-contact">
    <p class="contact-name">Lark Roofing</p>
    <p class="contact-phone">888.417.LARK</p>
  </div>
  <p class="text front-web">www.LarkRoofing.example</p>
</section>

<section class="postcard postcard--back" aria-label="Postcard back">
  <svg class="artwork" width="855" height="570" viewBox="0 0 855 570">
    <defs>
      <linearGradient id="crew-photo" x1="0" y1="0" x2="1" y2="1">
        <stop offset="0" stop-color="#5d7fa6"/>
        <stop offset="0.5" stop-color="var(--photo-roof)"/>
        <stop offset="1" stop-color="var(--photo-earth)"/>
      </linearGradient>
      <linearGradient id="tile-photo" x1="0" y1="0" x2="1" y2="1">
        <stop offset="0" stop-color="#4b4440"/>
        <stop offset="1" stop-color="#7a6456"/>
      </linearGradient>
    </defs>
    <polygon points="0,140 255,262 428,150 428,325 0,325" fill="var(--gold)"/>
    <polygon points="0,0 428,0 428,135 255,245 0,125" fill="url(#crew-photo)" role="img" aria-label="Photo of two roofers replacing damaged roof tiles"/>
    <polyline points="0,140 255,262 428,150" fill="none" stroke="var(--ink)" stroke-width="4"/>
    <polygon points="300,120 380,166 380,258 300,304 220,258 220,166" fill="var(--paper)" stroke="var(--gold)" stroke-width="5"/>
    <polygon points="300,134 368,173 368,251 300,290 232,251 232,173" fill="url(#tile-photo)" role="img" aria-label="Close-up photo of gloved hands fixing a roof tile"/>
    <rect x="0" y="325" width="428" height="90" fill="var(--charcoal)"/>
    <polygon points="0,465 0,570 155,570" fill="var(--steel-blue)"/>
    <polygon points="150,556 855,556 855,570 165,570" fill="var(--gold)"/>
    <rect x="718" y="42" width="92" height="92" fill="var(--stamp)"/>
  </svg>
  <p class="text offer">OFFER <strong>$200 OFF</strong> ANY REPAIR<small>*some rules may apply</small></p>
  <div class="text back-contact">
    <p class="contact-name">Lark Roofing</p>
    <p class="contact-phone">888.417.LARK</p>
    <p class="contact-web">www.LarkRoofing.example</p>
  </div>
  <p class="text brand-name back-brand">LARKROOFING.EXAMPLE</p>
</section>

</body>
</html>
```